Quillmark Hall Business Card

I need a business card design. We are a collaborate online training company. Our colors are gray and green. Our website is QuillmarkHall.com

I would like an area for a profile picture within the card

```html
<!DOCTYPE html>
<html lang="en">
<head>
<meta charset="utf-8">
<title>Quillmark Hall Business Card</title>
<link href="https://fonts.googleapis.com/css2?family=Lato:wght@400;700&display=swap" rel="stylesheet">
<style>
  :root {
    --stage: #2b2b2b;
    --card: #262d30;
    --green: #8dc63f;
    --white: #ffffff;
    --text-soft: #e9ecec;
    --photo-top: #3a4246;
    --photo-bottom: #55585c;
  }
  * { margin: 0; padding: 0; box-sizing: border-box; }
  html, body {
    width: 1200px; height: 1166px; overflow: hidden;
    background: var(--stage);
    font-family: "Lato", sans-serif;
  }
  .card {
    position: absolute;
    left: 180px;
    width: 840px; height: 480px;
    background: var(--card);
    overflow: hidden;
    box-shadow: 0 18px 40px rgba(0,0,0,0.45);
  }
  .card-back { top: 60px; }
  .card-front { top: 620px; }

  .brand {
    display: flex; align-items: center; gap: 16px;
    color: var(--green);
    font-weight: 700;
    letter-spacing: -1px;
    white-space: nowrap;
  }
  .brand-dot {
    border-radius: 50%;
    background: var(--green);
    flex: none;
  }
  .card-back .brand {
    position: absolute; left: 50%; top: 190px;
    transform: translateX(-50%);
    font-size: 76px;
  }
  .card-back .brand-dot { width: 70px; height: 70px; }
  .card-back .site {
    position: absolute; right: 150px; bottom: 110px;
    color: var(--text-soft); font-size: 22px; letter-spacing: 2px;
  }

  .card-front .brand {
    position: absolute; left: 50px; top: 60px;
    font-size: 54px; gap: 12px;
  }
  .card-front .brand-dot { width: 52px; height: 52px; }

  .profile-photo {
    position: absolute; right: 0; top: 0;
    width: 320px; height: 405px;
    background: linear-gradient(180deg, var(--photo-top), var(--photo-bottom));
  }

  .identity { position: absolute; left: 68px; top: 168px; }
  .person-name { color: var(--white); font-size: 32px; font-weight: 400; line-height: 1.1; }
  .person-role { color: var(--green); font-size: 22px; line-height: 1.2; }

  .address {
    position: absolute; left: 88px; top: 250px;
    color: var(--white); font-size: 22px; line-height: 1.25; font-style: normal;
  }
  .contacts {
    position: absolute; left: 88px; top: 320px;
    list-style: none;
    color: var(--white); font-size: 22px; line-height: 1.25;
  }
  .contacts li { display: flex; align-items: center; gap: 12px; }
  .contacts svg { width: 18px; height: 18px; fill: var(--green); flex: none; }

  .edge-bands { position: absolute; left: 0; top: 0; width: 840px; height: 480px; pointer-events: none; }
</style>
</head>
<body>

<section class="card card-back" aria-label="Card back">
  <div class="brand"><span class="brand-dot"></span>Quillmark Hall</div>
  <p class="site">www.quillmarkhall.com</p>
</section>

<section class="card card-front" aria-label="Card front">
  <div class="profile-photo" role="img" aria-label="Profile photo of the founder in a grey suit"></div>

  <svg class="edge-bands" viewBox="0 0 840 480" aria-hidden="true">
    <polygon points="0,452 540,452 562,405 840,405 840,396 556,396 534,444 0,444" fill="var(--green)"/>
    <polygon points="0,480 0,455 538,455 530,480" fill="var(--white)"/>
  </svg>

  <div class="brand"><span class="brand-dot"></span>Quillmark Hall</div>

  <div class="identity">
    <p class="person-name">Dorian Fell</p>
    <p class="person-role">Founder</p>
  </div>

  <address class="address">
    482 N Larkspur Ave. Suite 7<br>
    Ashford, Oregon 97031
  </address>

  <ul class="contacts">
    <li>
      <svg viewBox="0 0 24 24"><path d="M6.6 10.8a15 15 0 0 0 6.6 6.6l2.2-2.2a1 1 0 0 1 1-.25 11.4 11.4 0 0 0 3.6.57 1 1 0 0 1 1 1V20a1 1 0 0 1-1 1A17 17 0 0 1 3 4a1 1 0 0 1 1-1h3.5a1 1 0 0 1 1 1c0 1.25.2 2.45.57 3.57a1 1 0 0 1-.25 1z"/></svg>
      (541) 628-4930
    </li>
    <li>
      <svg viewBox="0 0 24 24"><path d="M2 5h20v14H2z M3.5 6.5 12 13l8.5-6.5" stroke="var(--card)" stroke-width="1.5"/></svg>
      info@quillmarkhall.com
    </li>
    <li>
      <svg viewBox="0 0 24 24"><circle cx="12" cy="12" r="10"/><path d="M2 12h20M12 2c3 3 3 17 0 20M12 2c-3 3-3 17 0 20" stroke="var(--card)" stroke-width="1.4" fill="none"/></svg>
      www.quillmarkhall.com
    </li>
  </ul>
</section>

</body>
</html>
```